Harbor Mortgage Relief

Please help us give our website a remake or a FACELIFT. It is not very good but it says what we need it to say. But the design is terrible.
I would like our new design font and logo to be used as the theme.

I also want more photos on the site.

I also want consistency with the pages so they look clean.

We want the professionals to do this, let's see what you got!

Thank you!
Updates

Project Deadline Extended
Reason: I can understand you want to be paid. So I will commit to the fee but I want you to have time to make a KICK ASS website for me dudes! Thanks

HI!  Just wanted to say thanks for your time on these.  A lot are great.  However the firefighters have nothing to do with Foreclosure.  We are saving peoples homes from the bank taking them and selling them.   I LOVE the house photos and the families on the website.  That is the direction we like.  THanks.

THANK U ALL FOR THE WORK!   I like a few ending in the numbers: 147  733  693  536  620  478  727  508     I will go over them and choose one soon.  Thank you.   You will be paid shortly. 

Requirements
Must have
• Bright, Upbeat photos. Color scheme should be in order. We like icons on the bottom. not just text.

```html
<!DOCTYPE html>
<html lang="en">
<head>
<meta charset="utf-8">
<title>Harbor Mortgage Relief</title>
<link rel="stylesheet" href="https://fonts.googleapis.com/css2?family=Open+Sans:wght@400;600;700&family=Tinos:ital@1&display=swap">
<style>
:root{
  --red:#a8323c;
  --red-deep:#7a1019;
  --red-dark:#5e0910;
  --pink:#e9aab0;
  --rule:#d9d2b8;
  --text:#333333;
  --heading:#7a1019;
  --white:#ffffff;
}
*{margin:0;padding:0;box-sizing:border-box}
html,body{width:1038px;height:1200px;overflow:hidden;background:var(--white)}
body{position:relative;font-family:"Open Sans",Verdana,sans-serif;color:var(--text)}
.abs{position:absolute}
.hero-photo{left:0;top:0;width:1038px;height:560px}
.header-band{left:0;top:0;width:1038px;height:200px}
.brand{left:158px;top:72px;display:flex;align-items:center;gap:10px}
.brand-dot{width:56px;height:56px;border-radius:50%;background:var(--red-dark)}
.brand-name{font-size:17px;font-weight:700;color:var(--red-dark);line-height:1.1;width:150px}
.phone{left:616px;top:29px;color:var(--white);font-size:15px;font-weight:600;letter-spacing:.3px}
.tagline{left:138px;top:362px;font-family:"Tinos",Georgia,serif;font-style:italic;font-size:23px;color:#3a3a3a}
.slider-dots{left:198px;top:474px;display:flex;gap:12px}
.slider-dots span{width:13px;height:13px;border-radius:50%;background:#7d7d7d}
.slider-dots span.active{background:#f0c419}
.main-nav{left:84px;top:542px;width:642px;height:75px;border-radius:14px 14px 6px 6px;
  background:linear-gradient(#b95760,var(--red) 45%,var(--red-deep));display:flex;box-shadow:0 2px 3px rgba(0,0,0,.25)}
.main-nav a{color:var(--white);text-decoration:none;font-size:14px;display:flex;align-items:flex-end;justify-content:center;padding-bottom:20px;border-right:1px solid rgba(0,0,0,.18);border-left:1px solid rgba(255,255,255,.12)}
.main-nav a:last-child{border-right:none}
.section-title{font-size:21px;font-weight:400;color:var(--text)}
.section-title em{font-style:normal;color:var(--heading)}
.rule{height:1px;background:var(--rule)}
.body-copy{font-size:13.5px;line-height:20px;letter-spacing:1px;text-align:justify}
.welcome-photo{left:86px;top:708px;width:175px;height:97px;border:2px solid #9a9a9a;
  background:linear-gradient(100deg,#8c7a6a 0%,#d9b59a 30%,#f0d6c2 50%,#e8e2dc 70%,#8e9aa4 100%)}
.more-btn{width:70px;height:24px;border-radius:3px;background:linear-gradient(#b5424c,var(--red-deep));color:#f4d9dc;font-size:12px;font-weight:600;display:flex;align-items:center;justify-content:center;gap:6px;box-shadow:0 1px 2px rgba(0,0,0,.3)}
.more-btn svg{width:7px;height:9px}
.profile-strip{left:87px;top:963px;width:638px;height:117px;border-radius:6px;background:linear-gradient(var(--red-deep),var(--red-dark));border:2px solid #c99}
.profile-thumb{top:14px;height:89px;border:2px solid #bfc7d4;background:linear-gradient(#2f6fd0 0%,#7fb0e6 30%,#e8e6e2 50%,#d8d0c4 70%,#4f8a34 85%,#3d6e28 100%)}
.strip-arrow{top:44px;width:10px;height:22px}
.news-item{width:253px}
.news-head{font-size:13px;font-weight:700;letter-spacing:1px;color:#3a3a3a}
.news-date{text-align:right;font-size:13px;letter-spacing:1px;margin-top:2px}
.footer-band{left:0;top:1090px;width:1038px;height:110px}
.copyright{left:89px;top:1168px;font-size:11.5px;color:var(--white)}
.copyright i{text-decoration:underline}
.footer-nav{left:542px;top:1164px;font-size:13.5px;color:var(--white);letter-spacing:.5px;display:flex;gap:12px}
.footer-nav a{color:var(--white);text-decoration:none}
.footer-nav a.current{text-decoration:underline}
</style>
</head>
<body>

<div class="abs hero-photo" role="img" aria-label="Smiling family of four standing in front of a large brick suburban house under a bright sky">
  <svg width="1038" height="560" viewBox="0 0 1038 560">
    <defs>
      <linearGradient id="heroTone" x1="0" y1="0" x2="0.25" y2="1">
        <stop offset="0" stop-color="#f4f8fc"/>
        <stop offset=".3" stop-color="#dce8f2"/>
        <stop offset=".5" stop-color="#d8cdb8"/>
        <stop offset=".72" stop-color="#b08e72"/>
        <stop offset="1" stop-color="#6e5444"/>
      </linearGradient>
    </defs>
    <path d="M0 0H1038V545C900 548 760 560 640 548C500 534 380 500 260 512C160 520 60 540 0 540Z" fill="url(#heroTone)"/>
    <path d="M0 540C60 540 160 520 260 512C380 500 500 534 640 548C760 560 900 548 1038 545" fill="none" stroke="var(--pink)" stroke-width="5"/>
  </svg>
</div>

<svg class="abs header-band" viewBox="0 0 1038 200" aria-hidden="true">
  <defs>
    <linearGradient id="bandTone" x1="0" y1="0" x2="0" y2="1">
      <stop offset="0" stop-color="#d0707a"/>
      <stop offset="1" stop-color="var(--red-deep)"/>
    </linearGradient>
  </defs>
  <path d="M0 0H1038V40C860 55 640 120 480 165C400 188 330 192 250 184C150 174 60 150 0 128Z" fill="url(#bandTone)"/>
  <path d="M1038 40C860 55 640 120 480 165C400 188 330 192 250 184C150 174 60 150 0 128" fill="none" stroke="var(--pink)" stroke-width="5"/>
</svg>

<div class="abs brand">
  <span class="brand-dot"></span>
  <span class="brand-name">Harbor Mortgage Relief</span>
</div>
<div class="abs phone">Call Toll Free Now : 800-555-0142</div>

<div class="abs tagline">homes that makes a family happy...</div>
<div class="abs slider-dots"><span></span><span class="active"></span><span></span></div>

<nav class="abs main-nav">
  <a href="#" style="width:109px">Home</a>
  <a href="#" style="width:115px">About Us</a>
  <a href="#" style="width:132px">Contact Us</a>
  <a href="#" style="width:119px">Services</a>
  <a href="#" style="width:167px">Financial Option</a>
</nav>

<h2 class="abs section-title" style="left:87px;top:655px"><em>Welcome</em> to our site</h2>
<div class="abs rule" style="left:84px;top:692px;width:642px"></div>
<div class="abs welcome-photo" role="img" aria-label="Smiling customer service representative at a desk"></div>
<p class="abs body-copy" style="left:280px;top:704px;width:441px">Please help us give our website a remake or a FACELIFT. It is not very good but it says what we need it to say. But the design is terrible. I would like our new design font and logo to be used as the theme. Please help us give our website a remake or a FACELIFT.</p>
<p class="abs body-copy" style="left:86px;top:816px;width:635px">Please help us give our website a remake or a FACELIFT. It is not very good but it says what we need it to say. But the design is terrible.I would like our new design font and logo to be used as the theme. Please help us give our website a remake or a FACELIFT. It is not very good but it says what we need it to say.</p>
<div class="abs more-btn" style="left:648px;top:890px"><svg viewBox="0 0 7 9"><path d="M0 0L7 4.5L0 9Z" fill="#f4d9dc"/></svg>More</div>

<h2 class="abs section-title" style="left:87px;top:911px"><em>Our</em> Profiles</h2>
<div class="abs rule" style="left:84px;top:945px;width:642px"></div>
<div class="abs profile-strip">
  <svg class="abs strip-arrow" style="left:14px" viewBox="0 0 10 22"><path d="M9 1L1 11L9 21" fill="none" stroke="#f1d2d5" stroke-width="2"/></svg>
  <div class="abs profile-thumb" style="left:46px;width:117px" role="img" aria-label="Victorian style home with a green lawn"></div>
  <div class="abs profile-thumb" style="left:180px;width:127px" role="img" aria-label="White two storey house with palm trees"></div>
  <div class="abs profile-thumb" style="left:323px;width:117px" role="img" aria-label="Victorian style home with a green lawn"></div>
  <div class="abs profile-thumb" style="left:457px;width:127px" role="img" aria-label="White two storey house with palm trees"></div>
  <svg class="abs strip-arrow" style="left:610px" viewBox="0 0 10 22"><path d="M1 1L9 11L1 21" fill="none" stroke="#f1d2d5" stroke-width="2"/></svg>
</div>

<h2 class="abs section-title" style="left:752px;top:658px"><em>Latest</em> News</h2>
<div class="abs rule" style="left:752px;top:692px;width:253px"></div>
<div class="abs news-item" style="left:753px;top:702px">
  <div class="news-head">Headline goes here</div>
  <p class="body-copy">We need a website that is stylish and modern- clean lines are important.</p>
  <div class="news-date">31.11.2012</div>
</div>
<div class="abs news-item" style="left:753px;top:816px">
  <div class="news-head">Headline goes here</div>
  <p class="body-copy">We need a website that is stylish and modern- clean lines are important.</p>
  <div class="news-date">31.11.2012</div>
</div>
<div class="abs news-item" style="left:753px;top:931px">
  <div class="news-head">Headline goes here</div>
  <p class="body-copy">We need a website that is stylish and modern- clean lines are important.</p>
  <div class="news-date">31.11.2012</div>
</div>
<div class="abs more-btn" style="left:933px;top:1058px"><svg viewBox="0 0 7 9"><path d="M0 0L7 4.5L0 9Z" fill="#f4d9dc"/></svg>More</div>

<svg class="abs footer-band" viewBox="0 0 1038 110" aria-hidden="true">
  <defs>
    <linearGradient id="footTone" x1="0" y1="0" x2="0" y2="1">
      <stop offset="0" stop-color="#c75a64"/>
      <stop offset="1" stop-color="var(--red-deep)"/>
    </linearGradient>
  </defs>
  <path d="M0 28C200 20 380 6 560 8C760 10 920 30 1038 38V110H0Z" fill="url(#footTone)"/>
  <path d="M0 28C200 20 380 6 560 8C760 10 920 30 1038 38" fill="none" stroke="#f3dfc0" stroke-width="4"/>
</svg>
<div class="abs copyright">Copyright @ 2012, <i>Harbor Mortgage Relief</i></div>
<div class="abs footer-nav">
  <a href="#" class="current">home</a><span>|</span>
  <a href="#">about us</a><span>|</span>
  <a href="#">Services</a><span>|</span>
  <a href="#">Financial Option</a><span>|</span>
  <a href="#">contact us</a>
</div>

</body>
</html>
```